Pet Shop Website

website will need to have the following features:
• Photo Galleries of each species (Dogs, Cats, Birds, Fish, Reptiles, Rabbits) in a light box popup
o Each species may have several different categories for example:
 Fish
• Marine fish
• Fresh water
• tropical
• Cichlid
• Information Fact sheets of each species – Downloaded as a pdf which can be either
o Care Sheets
o Training Sheets
• Members Area
o Username (Email Address) & Password login
o New signups
o Exclusive Member Deals
o Newsletter options

The front page must be very simple (for example lumavest.com.au) contain the following:
• Product of the week - which can be purchased online
o Short details
o Cost
• Pet Club Sign up picture
• Animal of the week/month
• Contact Phone Number and addresses of the stores
• A jQuery slideshow (Images could include stores, pets etc…)
The main page MUST keep simple. We do not want it cluttered.

Inner Page
The animals / reptile page will need to have:
• Short description of the species
• Photo Galleries
• A list of what is in stock and the list needs to clearly be sorted by each store (Use of Tabs maybe).
• Facts sheets / Info sheets
The type of website ideas (not the type of look that we are necessary after) is and the sort of content that we want to offer are as follows:

http://www.scalenook.com.au/
http://www.brindlecovepaws.com.au/
http://www.thefurrowden.com.au
http://www.tailtown.net.au

Colour in the new website:
Blue
Red
Grey
Yellow

Original site:

http://www.critterglow.com.au
Updates

Hi Guys,

We had feedback from the client and they would like to see a few dark designs.

Thanks                                   

Reason: We would like to reopen this contest back up for a further week

Target Market(s)

Targeting animal lovers

Industry/Entity Type

Store

Requirements
Should not have
• Alter the logo in anyway

```html
<!DOCTYPE html>
<html lang="en">
<head>
<meta charset="utf-8">
<title>Critter Glow – Pet Superstores</title>
<link href="https://fonts.googleapis.com/css2?family=Amaranth:ital,wght@0,400;0,700;1,400;1,700&family=Open+Sans:ital,wght@0,400;0,600;0,700;1,400;1,700&display=swap" rel="stylesheet">
<style>
:root{
  --page-bg:#1f2c42;
  --panel:#ffffff;
  --red:#d0140f;
  --red-dark:#a80f0b;
  --navy:#24457a;
  --orange:#e85f1e;
  --crimson:#b3161c;
  --footer:#0f1a2b;
  --ink:#111;
  --muted:#555;
  --sky:#3ab0e6;
  --btn-blue:#5b8fd6;
}
*{box-sizing:border-box;margin:0;padding:0}
html,body{width:1200px;height:978px;overflow:hidden}
body{background:var(--page-bg);font-family:"Open Sans",Arial,sans-serif;position:relative}
.site{position:absolute;left:132px;top:19px;width:936px;height:807px;background:var(--panel);border-radius:14px 14px 0 0}
.abs{position:absolute}
.logo{left:30px;top:36px;display:flex;align-items:center;gap:10px;font-family:"Amaranth",sans-serif;font-weight:700;font-size:34px;color:var(--navy)}
.logo-mark{width:22px;height:22px;background:#f2d21a;border-radius:50%}
.social{left:614px;top:21px;width:131px;height:41px;background:#3b5a99;color:#fff;font-size:12px;line-height:14px;padding:6px 10px;font-weight:600}
.social b{font-size:15px;display:block}
.subscribe{left:755px;top:21px;width:131px;height:41px;background:#6b5348;color:#fff;font-size:10px;line-height:12px;padding:6px 10px;text-align:center}
.subscribe b{font-size:15px;display:block;line-height:17px}
.support{left:614px;top:77px;font-style:italic;color:var(--muted);font-size:17px}
.phones{left:614px;top:101px;font-style:italic;font-weight:700;color:var(--red);font-size:23px;letter-spacing:.3px}
.nav{left:10px;top:145px;width:916px;height:41px;background:linear-gradient(#e01a14,var(--red-dark));border-radius:12px 0 22px 0;display:flex;align-items:center;justify-content:space-around;padding:0 6px}
.nav a{color:#fff;text-decoration:none;font-family:Arial,sans-serif;font-weight:700;font-size:15px;text-transform:uppercase}
.slider{left:10px;top:202px;width:916px;height:289px;background:linear-gradient(180deg,#fff 0%,#f6f6f6 70%,#e9f3e3 100%);overflow:hidden}
.slide-art{position:absolute;right:20px;bottom:0;width:440px;height:289px;background:linear-gradient(90deg,#ece6df,#c69c74 60%,#8d6340);border-radius:40px 0 0 0}
.slide-band{position:absolute;left:0;bottom:0;width:480px;height:70px;background:linear-gradient(90deg,#e6f4e1,#8fd38a);clip-path:polygon(0 60%,100% 0,100% 100%,0 100%)}
.welcome{position:absolute;left:52px;top:44px;font-family:"Amaranth",sans-serif;font-size:29px;color:var(--ink);line-height:52px;white-space:nowrap}
.welcome .hl{display:block;padding-left:87px;color:var(--red);font-family:"Open Sans",sans-serif;font-weight:700;font-size:28px}
.welcome .loc{display:block;padding-left:6px}
.arrow{position:absolute;top:130px;width:17px;height:29px;background:#4a4a4a;color:#fff;display:flex;align-items:center;justify-content:center}
.arrow.prev{left:0}.arrow.next{right:0}
.card{top:527px;width:286px;height:222px;border-radius:0 0 14px 14px;overflow:hidden}
.card h2{height:38px;color:#fff;font-family:"Amaranth",sans-serif;font-weight:400;font-size:21px;padding:5px 18px;border-radius:4px 4px 0 0}
.card-body{position:relative;height:184px;padding:18px 18px}
.card-body p{position:relative;z-index:1;font-family:"Amaranth",sans-serif;font-style:italic;font-size:13px;line-height:17px;width:140px}
.card-art{position:absolute;right:8px;bottom:10px;width:105px;height:150px;border-radius:36px}
.pill{position:absolute;left:10px;bottom:12px;height:28px;padding:0 16px;border-radius:14px;background:linear-gradient(#f05a32,#c9200f);color:#fff;font-family:"Amaranth",sans-serif;font-style:italic;font-weight:700;font-size:16px;display:flex;align-items:center;border:2px solid #fff;box-shadow:0 1px 3px rgba(0,0,0,.3)}
.c1{left:10px}.c1 h2{background:var(--navy)}.c1 .card-body{background:linear-gradient(135deg,#dff2fc,#8fd1f0)}
.c1 .card-body p{color:var(--navy)}
.c1 h3{font-family:"Open Sans",sans-serif;font-weight:400;font-size:17px;color:#111;margin-bottom:8px}
.c1 .card-art{background:linear-gradient(#b9b3ab,#6f6a66)}
.c2{left:325px}.c2 h2{background:var(--orange)}.c2 .card-body{background:linear-gradient(135deg,#fbeed8,#f4cc86)}
.c2 .card-body p{color:#8a4c1a;padding-top:24px;width:120px}
.c2 .card-art{width:115px;background:linear-gradient(90deg,#a97a55,#efe9e2)}
.c3{left:641px}.c3 h2{background:var(--crimson)}.c3 .card-body{background:linear-gradient(135deg,#fde3ee,#f6b6cf)}
.c3 .card-body p{color:#9a2340;padding-top:24px}
.c3 .card-art{background:linear-gradient(#f2c94c,#59b8d8)}
.footer-band{position:absolute;left:132px;top:826px;width:936px;height:104px;background:var(--footer);border-radius:0 0 14px 14px}
.at{position:absolute;left:22px;top:24px;width:56px;height:56px;border:3px solid #2c3c55;border-radius:50%;color:#2c3c55;font-size:38px;display:flex;align-items:center;justify-content:center;font-weight:700}
.nl-title{position:absolute;left:94px;top:22px;color:#fff;font-size:19px}
.nl-text{position:absolute;left:94px;top:52px;color:var(--sky);font-size:11px;line-height:15px;width:170px}
.field{position:absolute;top:42px;width:198px;height:28px;border-radius:14px;background:#fff;border:3px solid #23324b;font-size:10px;color:#666;padding:4px 12px;font-weight:600}
.f1{left:324px}.f2{left:540px}
.send{position:absolute;left:768px;top:39px;width:130px;height:33px;border-radius:16px;background:var(--btn-blue);color:#fff;font-size:11px;font-weight:700;display:flex;align-items:center;justify-content:center}
.copyright{position:absolute;left:132px;top:946px;color:#fff;font-size:11px}
.species{position:absolute;right:136px;top:944px;color:#fff;font-size:11px}
.species span{margin:0 5px}
</style>
</head>
<body>
<div class="site">
  <div class="abs logo"><span class="logo-mark"></span>Critter Glow</div>
  <div class="abs social">Join us on<b>Pawsnet</b></div>
  <div class="abs subscribe"><b>Subscribe</b>to our newsletter</div>
  <div class="abs support">For Customer Support</div>
  <div class="abs phones">08.5550.1970 / 08.5550.6619</div>
  <nav class="abs nav">
    <a href="#">Home</a><a href="#">About Us</a><a href="#">Pets</a><a href="#">Marine Fish</a><a href="#">Fresh Water</a><a href="#">Tropical</a><a href="#">Cichlid</a><a href="#">Members Area</a><a href="#">Contact</a>
  </nav>
  <section class="abs slider">
    <div class="slide-band"></div>
    <div class="slide-art" role="img" aria-label="Group photo of dogs, cats, puppies, a rabbit and a bird sitting in a row"></div>
    <div class="welcome">Welcome to Critter Glow your<span class="hl">PET SUPERSTORES</span><span class="loc">@ Harrowfield &amp; Ashby Lake</span></div>
    <div class="arrow prev">&#8249;</div><div class="arrow next">&#8250;</div>
  </section>
  <article class="abs card c1">
    <h2>Product of the Week</h2>
    <div class="card-body">
      <h3>Domestic Kittens</h3>
      <p>Dolor sit amet, consecte adi pisci velit poriam est qui dolore...</p>
      <div class="card-art" role="img" aria-label="Photo of a grey long-haired kitten in a festive hat"></div>
      <div class="pill">$225.00</div>
    </div>
  </article>
  <article class="abs card c2">
    <h2>Pet Club Sign up</h2>
    <div class="card-body">
      <p>Consecte adi pisci velitse est ore...</p>
      <div class="card-art" role="img" aria-label="Photo of a rabbit and a puppy side by side"></div>
      <div class="pill">Sign Up &#10140;</div>
    </div>
  </article>
  <article class="abs card c3">
    <h2>Animal of the Week</h2>
    <div class="card-body">
      <p>Dolor sit amet, consecte adi pisci velit poriam est qui dolore...</p>
      <div class="card-art" role="img" aria-label="Photo of a small dog in sunglasses sitting on a blue suitcase"></div>
      <div class="pill">View More</div>
    </div>
  </article>
</div>
<footer class="footer-band">
  <div class="at">@</div>
  <div class="nl-title">Newsletter</div>
  <div class="nl-text">We will let you know when we implement new features.</div>
  <div class="field f1">Your Name:</div>
  <div class="field f2">Your Email Address:</div>
  <div class="send">SUBSCRIBE NOW!</div>
</footer>
<div class="copyright">Copyright © Critter Glow. All Rights Reserved.</div>
<div class="species">Reptiles<span>/</span>Fish<span>/</span>Dogs<span>/</span>Birds<span>/</span>Cats<span>/</span>Small Animals</div>
</body>
</html>
```